Rebranding: velvetlink.io | Online Dating Website

We need a rebranding of our existing website https://www.velvetlink.io

The site is an online dating platform, offering several services such as member search, chats and blog posts. The design should be similar, but more modern than our existing site.

Mobile First, so it should be highly usable on mobile devices!

Startpage and all public sites have to be SEO optimized for a high page speed.Registration is free, so you can take a look at all internal pages.

Target Market(s)

Global website users

Coding

Coded - Design and coding required

Number of Pages Required

5+ page

Requirements
Must have
• a bigger UI Framework like bootstrap or uikit as part of it

```html
<!DOCTYPE html>
<html lang="en">
<head>
<meta charset="utf-8">
<title>velvetlink.io – Online Dating</title>
<link rel="stylesheet" href="https://fonts.googleapis.com/css2?family=Rubik:wght@400;500;700&family=Hind:wght@300;400;500;600&display=swap">
<style>
:root{
  --pink:#e35fd3;
  --pink-dark:#d447c4;
  --pink-soft:#fcedf9;
  --ink:#1e1e24;
  --text:#6b6b72;
  --white:#ffffff;
  --line:#dddddd;
}
*{box-sizing:border-box;margin:0;padding:0}
html,body{width:1200px;height:2474px;overflow:hidden;background:var(--white)}
body{position:relative;font-family:"Hind",sans-serif;color:var(--text)}
.abs{position:absolute}

/* header */
.site-header{left:0;top:0;width:1200px;height:128px;background:var(--white)}
.brand{display:flex;align-items:center;gap:10px;font-family:"Hind",sans-serif;font-weight:400;font-size:22px;letter-spacing:1px;color:#333}
.brand .dot{width:16px;height:16px;border-radius:50%;background:var(--pink)}
.header-brand{left:110px;top:50px}
.btn{display:flex;align-items:center;justify-content:center;border-radius:24px;font-family:"Rubik",sans-serif;font-weight:700;font-size:14px;letter-spacing:.5px}
.btn-register{left:821px;top:42px;width:130px;height:46px;background:var(--pink);color:var(--white)}
.btn-login{left:958px;top:42px;width:130px;height:46px;border:2px solid var(--pink);color:var(--ink);gap:6px;box-shadow:0 3px 8px rgba(227,95,211,.25)}

/* sidebar */
.sidebar{left:0;top:128px;width:343px;height:2346px;background:var(--pink-soft)}
.nav-item{left:0;width:343px;height:68px;display:flex;align-items:center;font-family:"Rubik",sans-serif;font-weight:700;font-size:20px;color:var(--ink)}
.nav-item svg{position:absolute;left:49px;top:24px}
.nav-item span{position:absolute;left:103px}
.nav-item.active{background:var(--pink);color:var(--white);border-radius:0 34px 34px 0}
.nav-item .go{position:absolute;right:8px;top:9px;width:50px;height:50px;border-radius:50%;background:var(--white)}

/* hero */
.hero{left:343px;top:128px;width:857px;height:627px;background:radial-gradient(ellipse at 70% 35%,#b0795a 0%,#6a4030 45%,#2e1c16 100%)}
.hero-eyebrow{left:423px;top:293px;font-family:"Rubik",sans-serif;font-weight:500;font-size:21px;color:var(--white)}
.hero-title{left:423px;top:325px;font-family:"Rubik",sans-serif;font-weight:700;font-size:46px;color:var(--white)}
.hero-list{left:423px;top:400px;list-style:none}
.hero-list li{display:flex;align-items:center;gap:20px;height:39.5px;font-size:19.5px;color:var(--white)}
.btn-join{left:423px;top:539px;width:130px;height:45px;background:var(--pink);color:var(--white);font-size:15px}

/* about */
.about-photo{left:426px;top:841px;width:355px;height:423px;background:linear-gradient(160deg,#d9d2c8,#b59c86 55%,#8c7060);border:3px solid var(--white);box-shadow:0 0 10px rgba(227,95,211,.25)}
.about-title{left:836px;top:857px;font-family:"Rubik",sans-serif;font-weight:700;font-size:35px;color:var(--ink)}
.about-title em{font-style:normal;color:var(--pink)}
.copy p{font-size:14.6px;line-height:25px;text-align:justify;margin-bottom:11px;font-weight:300;color:#555}
.about-copy{left:836px;top:918px;width:252px}
.intro-copy{left:423px;top:1305px;width:665px}
.intro-copy p{margin-bottom:16px}

/* news */
.news{left:343px;top:1816px;width:857px;height:459px;background:linear-gradient(90deg,#e25cd2,#e665d6 60%,#e05ad0)}
.news-title{left:421px;top:1884px;font-family:"Rubik",sans-serif;font-weight:700;font-size:34px;color:var(--white)}
.news-card{top:1955px;width:210px;height:152px;border:3px solid var(--white)}
.news-caption{top:2087px;width:184px;height:110px;background:var(--white);display:flex;align-items:center;justify-content:center;text-align:center;padding:0 16px;font-family:"Hind",sans-serif;font-weight:600;font-size:15px;line-height:24px;color:var(--ink)}

/* footer */
.footer-brand{left:422px;top:2345px;font-size:24px}
.footer-links{right:112px;width:420px;text-align:right;font-size:12.5px;font-weight:500;color:var(--ink);line-height:24px;top:2337px}
.footer-links .sep{margin:0 16px}
.footer-rule{left:343px;top:2422px;width:857px;height:1px;background:var(--line)}
.copyright{left:343px;top:2435px;width:857px;text-align:center;font-size:12px;color:#555}
.copyright b{font-weight:500;color:var(--ink)}
.chat-bubble{left:1121px;top:2360px;width:43px;height:43px;border-radius:50%;background:var(--pink);box-shadow:0 2px 8px rgba(0,0,0,.2);display:flex;align-items:center;justify-content:center}
</style>
</head>
<body>

<header class="site-header abs">
  <div class="brand header-brand abs"><i class="dot"></i>VELVETLINK.IO</div>
  <a class="btn btn-register abs">REGISTER</a>
  <a class="btn btn-login abs">
    <svg width="12" height="13" viewBox="0 0 12 13"><circle cx="6" cy="3.5" r="3" fill="#1e1e24"/><path d="M0 13c0-4 2.5-6 6-6s6 2 6 6z" fill="#1e1e24"/></svg>LOGIN</a>
</header>

<nav class="sidebar abs"></nav>
<a class="nav-item active abs" style="top:200px">
  <svg width="20" height="20" viewBox="0 0 20 20"><path d="M10 3 2 10h2.5v7h4v-4h3v4h4v-7H18z" fill="#fff"/></svg>
  <span>HOME</span>
  <i class="go"><svg width="50" height="50" viewBox="0 0 50 50"><circle cx="25" cy="25" r="9" fill="#1e1e24"/><path d="M20 25h9m-3.5-4 4 4-4 4" stroke="#fff" stroke-width="2.4" fill="none" stroke-linecap="round"/></svg></i>
</a>
<a class="nav-item abs" style="top:290px"><svg width="20" height="20" viewBox="0 0 20 20"><circle cx="8.5" cy="8.5" r="5.5" stroke="#e35fd3" stroke-width="2.6" fill="none"/><path d="m12.5 12.5 5 5" stroke="#e35fd3" stroke-width="3" stroke-linecap="round"/></svg><span>SUGARGIRLS</span></a>
<a class="nav-item abs" style="top:380px"><svg width="20" height="20" viewBox="0 0 20 20"><path d="M4 1h8l4 4v14H4z" fill="none" stroke="#e35fd3" stroke-width="1.6"/><path d="M7 9h6M7 12h6M7 15h6" stroke="#e35fd3" stroke-width="1.4"/></svg><span>PIN BOARD</span></a>
<a class="nav-item abs" style="top:470px"><svg width="20" height="20" viewBox="0 0 20 20"><path d="M1 9c0-4 2-6 5-6v3c-1.5 0-2 1-2 3h3v7H1zM11 9c0-4 2-6 5-6v3c-1.5 0-2 1-2 3h3v7h-6z" fill="#e35fd3"/></svg><span>TESTIMONIALS</span></a>
<a class="nav-item abs" style="top:560px"><svg width="22" height="20" viewBox="0 0 22 20"><rect x="3" y="3" width="18" height="14" fill="none" stroke="#e35fd3" stroke-width="1.6"/><path d="M3 6H1v11h2" fill="none" stroke="#e35fd3" stroke-width="1.4"/><rect x="6" y="6" width="6" height="5" fill="#e35fd3"/><path d="M14 7h5M14 10h5M6 14h13" stroke="#e35fd3" stroke-width="1.4"/></svg><span>NEWS</span></a>
<a class="nav-item abs" style="top:650px"><svg width="20" height="20" viewBox="0 0 20 20"><circle cx="10" cy="10" r="8" fill="#e35fd3"/><path d="M7.5 8a2.5 2.5 0 1 1 3.5 2.3c-.7.4-1 .8-1 1.7" stroke="#fff" stroke-width="1.8" fill="none"/><circle cx="10" cy="14.5" r="1.1" fill="#fff"/></svg><span>FAQ</span></a>
<a class="nav-item abs" style="top:740px"><svg width="20" height="20" viewBox="0 0 20 20"><rect x="1" y="4" width="18" height="13" rx="1.5" fill="#e35fd3"/><path d="m1.5 5 8.5 6 8.5-6" stroke="#fff" stroke-width="1.6" fill="none"/></svg><span>CONTACT</span></a>

<section class="hero abs" role="img" aria-label="Photo of a smiling couple embracing at a candlelit table"></section>
<div class="hero-eyebrow abs">WELCOME TO</div>
<h1 class="hero-title abs">VELVETLINK.IO</h1>
<ul class="hero-list abs">
  <li><svg width="17" height="17" viewBox="0 0 17 17"><circle cx="8.5" cy="8.5" r="8.5" fill="#e35fd3"/><path d="m5 8.7 2.4 2.4L12 6.5" stroke="#fff" stroke-width="2" fill="none"/></svg>Thousands of members in our community</li>
  <li><svg width="17" height="17" viewBox="0 0 17 17"><circle cx="8.5" cy="8.5" r="8.5" fill="#e35fd3"/><path d="m5 8.7 2.4 2.4L12 6.5" stroke="#fff" stroke-width="2" fill="none"/></svg>Free to sign-up, create a profile and write posts</li>
  <li><svg width="17" height="17" viewBox="0 0 17 17"><circle cx="8.5" cy="8.5" r="8.5" fill="#e35fd3"/><path d="m5 8.7 2.4 2.4L12 6.5" stroke="#fff" stroke-width="2" fill="none"/></svg>High security &amp; verification process</li>
</ul>
<a class="btn btn-join abs">JOIN FREE</a>

<div class="about-photo abs" role="img" aria-label="Photo of a laughing couple, woman on the man's back at the beach"></div>
<h2 class="about-title abs">ABOUT <em>US</em></h2>
<div class="copy about-copy abs">
  <p>velvetlink.io is a sugardaddy app designed to connect people who are interested in any kind of Sugar Daddy Online Arrangements.</p>
  <p>It's about virtual companionships, chats and conversations as well as exchanging customized content between real members.</p>
  <p>Ever asked yourself "Where can i find a sugar daddy for me?" You have come to the right place! Find your cyber sugar daddy!!</p>
</div>
<div class="copy intro-copy abs">
  <p>velvetlink.io is the premier online destination for finding the perfect sugar daddy. Whether you're a young woman looking for financial support or a mature woman seeking a mutually beneficial relationship, velvetlink.io has something for everyone.</p>
  <p>With a user-friendly interface and advanced search features, it's easy to find exactly what you're looking for. Simply create a free profile and start browsing through the thousands of potential sugar daddies in your area.</p>
  <p>At velvetlink.io, your safety and privacy are our top priority. All profiles are verified to ensure authenticity and our team is available 24/7 to answer any questions or concerns.</p>
  <p>Don't waste your time on generic dating apps or sites. velvetlink.io is specifically designed for those seeking a sugar daddy relationship. Join today and find the perfect sugar daddy for you.</p>
  <p>In addition, the website is mobile-friendly and can be easily access via any device including smartphones and tablets, making it easy to stay connected and find a match on the go.</p>
  <p>Join the thousands of successful women who have found the perfect sugar daddy at velvetlink.io. Sign up now and start living the life you deserve.</p>
</div>

<section class="news abs"></section>
<h2 class="news-title abs">LATEST NEWS</h2>
<div class="news-card abs" style="left:423px;background:linear-gradient(120deg,#e8e6e4,#c9b8ad)" role="img" aria-label="Photo of a woman smiling at her laptop"></div>
<div class="news-card abs" style="left:652px;background:linear-gradient(180deg,#8ea3b8,#4c5868)" role="img" aria-label="Photo of a couple looking at a phone by the sea"></div>
<div class="news-card abs" style="left:880px;background:linear-gradient(180deg,#8fc0e0,#d9c7b2)" role="img" aria-label="Photo of a couple on a sunny beach"></div>
<div class="news-caption abs" style="left:436px">Your Go-To Guide to Finding a Sugar Daddy Online</div>
<div class="news-caption abs" style="left:665px">What is a sugar daddy?</div>
<div class="news-caption abs" style="left:893px">Sugar Daddy Websites Without Meeting Advisory</div>

<footer>
  <div class="brand footer-brand abs"><i class="dot"></i>VELVETLINK.IO</div>
  <div class="footer-links abs">
    PRIVACY POLICY<span class="sep">|</span>TERMS &amp; CONDITIONS<span class="sep">|</span>IMPRINT<span class="sep">|</span><br>
    CONTACT<span class="sep">|</span>COOKIE SETTINGS
  </div>
  <div class="footer-rule abs"></div>
  <div class="copyright abs">© 2023 <b>VELVETLINK.IO</b> &nbsp;-&nbsp; All Rights Reserved</div>
  <div class="chat-bubble abs"><svg width="22" height="18" viewBox="0 0 22 18"><ellipse cx="9" cy="7" rx="8" ry="6" fill="#fff"/><path d="M4 11 2 16l6-3z" fill="#fff"/><path d="M18 7c3 1 4 3 3 5l1 4-4-2c-2 1-5 0-6-1" fill="#fff"/></svg></div>
</footer>

</body>
</html>
```